Vardell Therapeutics is a biotech company that needs a slide deck theme.

We need a slide deck theme with several different slide templates we could use for presentation of data or research ideas. Our logo is attached. We picked "Vardell" as our company name because we use epigenome editing tools to fine-tune gene expression for therapeutic purposes. Our logo color is a seafoam green, and we would like to see this color along with other colors that could complement it well. Keywords: genetics, biotech, cells, human therapies,

```html
<!DOCTYPE html>
<html lang="en">
<head>
<meta charset="utf-8">
<title>Vardell Therapeutics – Content Slide</title>
<link rel="stylesheet" href="https://fonts.googleapis.com/css2?family=Open+Sans:wght@300;400&family=Carlito:wght@400;700&display=swap">
<style>
  :root {
    --slate: #353849;
    --seafoam: #1fc2b1;
    --seafoam-bright: #00cfb8;
    --ocean: #0079ae;
    --coral: #ff8570;
    --cream: #f8f6dc;
    --paper: #f5f5f6;
    --ink: #3a3d4c;
    --body-text: #e4e5ea;
    --chart-text: #ffffff;
  }
  * { margin: 0; padding: 0; box-sizing: border-box; }
  html, body {
    width: 1200px;
    height: 675px;
    overflow: hidden;
    background: var(--slate);
  }
  .slide {
    position: relative;
    width: 1200px;
    height: 675px;
    background: var(--slate);
    font-family: "Open Sans", sans-serif;
  }
  .slide-title {
    position: absolute;
    left: 91px;
    top: 44px;
    font-weight: 300;
    font-size: 34px;
    color: var(--seafoam);
    letter-spacing: 0.3px;
  }
  .title-rule {
    position: absolute;
    left: 75px;
    top: 95px;
    width: 1052px;
    height: 3px;
    background: var(--seafoam);
  }
  .body-copy {
    position: absolute;
    left: 92px;
    top: 184px;
    width: 440px;
    font-size: 17.6px;
    line-height: 27.2px;
    letter-spacing: 0.2px;
    color: var(--body-text);
  }
  .artwork {
    position: absolute;
    inset: 0;
  }
  .chart-title {
    font-family: "Carlito", sans-serif;
    font-weight: 700;
    font-size: 23px;
    fill: var(--chart-text);
  }
  .legend-label {
    font-family: "Carlito", sans-serif;
    font-size: 13.5px;
    fill: var(--chart-text);
  }
  .brand {
    position: absolute;
    left: 200px;
    top: 603px;
    display: flex;
    align-items: center;
    gap: 16px;
  }
  .brand-dot {
    width: 56px;
    height: 56px;
    border-radius: 50%;
    background: var(--seafoam);
  }
  .brand-name {
    font-weight: 400;
    font-size: 24px;
    letter-spacing: 2px;
    color: var(--ink);
    text-transform: uppercase;
  }
  .page-number {
    position: absolute;
    right: 56px;
    top: 627px;
    font-size: 26px;
    color: var(--ink);
  }
</style>
</head>
<body>
<main class="slide">
  <h1 class="slide-title">Title 1</h1>
  <div class="title-rule"></div>

  <p class="body-copy">We need a slide deck theme with several different slide templates we could use for presentation of data or research ideas. Our logo is attached. We picked "Vardell" as our company name because we use epigenome editing tools to fine-tune gene expression for therapeutic purposes. Our logo color is a seafoam green, and we would like to see this color along with other colors that could complement it well. Keywords: genetics, biotech, cells, human therapies,</p>

  <svg class="artwork" width="1200" height="675" viewBox="0 0 1200 675">
    <defs>
      <filter id="pie-shadow" x="-20%" y="-20%" width="140%" height="140%">
        <feDropShadow dx="0" dy="2" stdDeviation="3" flood-color="#000" flood-opacity="0.35"/>
      </filter>
    </defs>

    <text class="chart-title" x="859" y="191" text-anchor="middle">Sales</text>
    <g class="pie" filter="url(#pie-shadow)">
      <path d="M859,351 L859,214 A137,137 0 1,1 788.4,468.4 Z" fill="var(--seafoam-bright)"/>
      <path d="M859,351 L788.4,468.4 A137,137 0 0,1 732.9,297.5 Z" fill="var(--ocean)"/>
      <path d="M859,351 L732.9,297.5 A137,137 0 0,1 788.4,233.6 Z" fill="var(--coral)"/>
      <path d="M859,351 L788.4,233.6 A137,137 0 0,1 859,214 Z" fill="var(--cream)"/>
    </g>
    <g class="legend">
      <rect x="727" y="509" width="9" height="9" fill="var(--seafoam-bright)"/>
      <text class="legend-label" x="740" y="518">1st Qtr</text>
      <rect x="796" y="509" width="9" height="9" fill="var(--ocean)"/>
      <text class="legend-label" x="809" y="518">2nd Qtr</text>
      <rect x="870" y="509" width="9" height="9" fill="var(--coral)"/>
      <text class="legend-label" x="883" y="518">3rd Qtr</text>
      <rect x="940" y="509" width="9" height="9" fill="var(--cream)"/>
      <text class="legend-label" x="953" y="518">4th Qtr</text>
    </g>

    <path class="footer-band" d="M0,624 C200,580 380,565 560,590 C760,620 940,665 1200,548 L1200,675 L0,675 Z" fill="var(--paper)"/>
    <path class="footer-edge" d="M0,620 C200,576 380,561 560,586 C760,616 940,661 1200,544" fill="none" stroke="var(--seafoam)" stroke-width="2" opacity="0.8"/>
  </svg>

  <div class="brand">
    <span class="brand-dot"></span>
    <span class="brand-name">Vardell Therapeutics</span>
  </div>
  <div class="page-number">24</div>
</main>
</body>
</html>
```